Business card for auto dealership

Looking for a clean modern design.
Would like attached logo incorporated

Industry/Entity Type

Car dealership

Contact Information for Business Card

Name, website, phone, cell, fax, email

```html
<!DOCTYPE html>
<html lang="en">
<head>
<meta charset="utf-8">
<title>Halvern Truck &amp; Auto Sales — Business Card</title>
<link href="https://fonts.googleapis.com/css2?family=Montserrat:wght@400;600;700&display=swap" rel="stylesheet">
<style>
  :root {
    --backdrop: #3a3a3a;
    --card-light: #ffffff;
    --card-dark: #111111;
    --ink: #141414;
    --ink-soft: #333333;
    --rule: #9a9a9a;
    --paper-text: #ffffff;
  }
  * { box-sizing: border-box; margin: 0; padding: 0; }
  html, body {
    width: 1200px; height: 1200px; overflow: hidden;
    background: var(--backdrop);
    font-family: "Montserrat", Arial, sans-serif;
  }
  .stage { position: relative; width: 1200px; height: 1200px; }

  .card {
    position: absolute; left: 250px; width: 700px; height: 400px;
    border-radius: 28px; overflow: hidden;
    box-shadow: 0 18px 40px rgba(0,0,0,.45);
  }
  .card--front { top: 150px; background: var(--card-light); color: var(--ink); }
  .card--back  { top: 650px; background: var(--card-dark); color: var(--paper-text); }

  /* brand name set as plain text */
  .brand {
    font-weight: 700; text-transform: uppercase; letter-spacing: .04em;
    line-height: 1.1;
  }
  .card--front .brand {
    position: absolute; left: 0; right: 0; top: 58px; text-align: center;
    font-size: 34px; color: var(--ink);
  }
  .card--front .brand-sub { display: block; font-size: 16px; letter-spacing: .16em; margin-top: 6px; }
  .top-rule {
    position: absolute; left: 60px; right: 60px; top: 160px;
    height: 1px; background: var(--rule);
  }

  .identity {
    position: absolute; left: 60px; top: 198px;
    border-left: 4px solid var(--ink); padding-left: 12px;
  }
  .identity .name { font-size: 26px; font-weight: 600; letter-spacing: .01em; }
  .identity .role { font-size: 13px; letter-spacing: .08em; color: var(--ink-soft); margin-top: 2px; }

  .mid-rule {
    position: absolute; left: 60px; width: 280px; top: 272px;
    height: 1px; background: var(--rule);
  }

  .contacts { position: absolute; list-style: none; }
  .contacts--left { left: 60px; top: 292px; }
  .contacts--right { left: 380px; top: 210px; }
  .contacts li {
    display: flex; align-items: center; gap: 12px;
    font-size: 19px; color: var(--ink-soft); height: 34px;
  }
  .contacts svg { width: 20px; height: 20px; flex: none; fill: var(--ink); }

  .card--back .brand {
    position: absolute; left: 0; right: 0; top: 130px; text-align: center;
    font-size: 52px;
  }
  .card--back .brand-sub { display: block; font-size: 22px; letter-spacing: .16em; margin-top: 10px; }
  .card--back .site {
    position: absolute; left: 0; right: 0; bottom: 52px; text-align: center;
    font-size: 22px; font-weight: 400; letter-spacing: .06em;
  }
</style>
</head>
<body>
<main class="stage">

  <section class="card card--front" aria-label="Card front">
    <h1 class="brand">Halvern<span class="brand-sub">Truck &amp; Auto Sales</span></h1>
    <div class="top-rule"></div>

    <div class="identity">
      <p class="name">DANA HALVERN</p>
      <p class="role">POSITION</p>
    </div>
    <div class="mid-rule"></div>

    <ul class="contacts contacts--left">
      <li>
        <svg viewBox="0 0 24 24" aria-label="Phone"><path d="M6.6 10.8a15.1 15.1 0 0 0 6.6 6.6l2.2-2.2c.3-.3.7-.4 1-.2 1.1.4 2.3.6 3.6.6.6 0 1 .4 1 1V20c0 .6-.4 1-1 1A17 17 0 0 1 3 4c0-.6.4-1 1-1h3.5c.6 0 1 .4 1 1 0 1.3.2 2.5.6 3.6.1.3 0 .7-.2 1l-2.3 2.2z"/></svg>
        555-210-4011
      </li>
      <li>
        <svg viewBox="0 0 24 24" aria-label="Mobile"><path d="M7 1h10a2 2 0 0 1 2 2v18a2 2 0 0 1-2 2H7a2 2 0 0 1-2-2V3a2 2 0 0 1 2-2zm0 3v14h10V4H7zm5 15.2a1 1 0 1 0 0 2 1 1 0 0 0 0-2z"/></svg>
        555-310-2140
      </li>
    </ul>

    <ul class="contacts contacts--right">
      <li>
        <svg viewBox="0 0 24 24" aria-label="Fax"><path d="M6 2h9l3 3v5h2a2 2 0 0 1 2 2v8a2 2 0 0 1-2 2H4a2 2 0 0 1-2-2v-8a2 2 0 0 1 2-2h2V2zm2 2v6h8V6h-3V4H8zm-3 9v2h2v-2H5zm4 0v2h2v-2H9zm4 0v6h6v-6h-6zM5 17v2h2v-2H5zm4 0v2h2v-2H9z"/></svg>
        555-410-1774
      </li>
      <li>
        <svg viewBox="0 0 24 24" aria-label="Email"><path d="M2 5h20v14H2V5zm2 2v.4l8 5.3 8-5.3V7H4zm16 2.8-8 5.3-8-5.3V17h16V9.8z"/></svg>
        dana@halvernauto.com
      </li>
    </ul>
  </section>

  <section class="card card--back" aria-label="Card back">
    <h2 class="brand">Halvern<span class="brand-sub">Truck &amp; Auto Sales</span></h2>
    <p class="site">HALVERNAUTO.COM</p>
  </section>

</main>
</body>
</html>
```